Pop punk gig poster design!

In need of an amazing poster design for a gig We are organising, the genre is pop punk, and will be an all ages gig. I need to it bold, random and capture the eye of any bypasses, and make people want to go to the gig just because the poster is awesome! The event will be called "A night of comets" and will consist of three bands and an acoustic set to open. All the bands are full of energy and create an unreal ambiance during there shows, I would like to capture that in the poster. Open to anything spectacular, the sky is the limit.

Requirements
Must have
• I need to have the name of the event "A Night Of Comets"
Band names(in this order):
-Turn the Dial
-Frozen Fenwick
-Wilma's Lantern
-Loralie Pettigrew

Date: Saturday 10th November 2012
Time: 5:15pm
Venue: The Kiln, 47 Tamsin street, West End, QLD 4101
Ticket price: $10+bf online
$15 at the door.
Free BBQ

```html
<!DOCTYPE html>
<html lang="en">
<head>
<meta charset="utf-8">
<title>A Night Of Comets – Gig Poster</title>
<link href="https://fonts.googleapis.com/css2?family=Audiowide&family=Frijole&family=Rye&family=Russo+One&family=Dosis:wght@700&display=swap" rel="stylesheet">
<style>
  :root {
    --sun: #fbe13a;
    --gold: #f7c51a;
    --amber: #f0a010;
    --rust: #d26a08;
    --ink: #111008;
    --olive: #3b3512;
    --band-fill: #efc82c;
    --white: #ffffff;
  }
  html, body {
    margin: 0;
    padding: 0;
    overflow: hidden;
    background: var(--ink);
  }
  .poster {
    position: relative;
    width: 848px;
    height: 1200px;
    overflow: hidden;
    background:
      radial-gradient(ellipse 45% 35% at 62% 30%, rgba(251,225,58,0.95) 0%, rgba(251,225,58,0) 100%),
      radial-gradient(ellipse 80% 65% at 50% 40%, var(--gold) 0%, var(--amber) 55%, var(--rust) 100%);
  }
  .skyline-strip {
    position: absolute;
    left: 48px;
    top: 6px;
    width: 780px;
    height: 52px;
    background: linear-gradient(180deg, rgba(17,16,8,0.35), rgba(17,16,8,0.8));
  }
  .event-title {
    position: absolute;
    left: 0;
    top: 78px;
    width: 848px;
    height: 70px;
  }
  .event-title text {
    font-family: "Audiowide", sans-serif;
    font-size: 54px;
    fill: var(--ink);
  }
  .event-title line { stroke: var(--ink); stroke-width: 2; }
  .tagline {
    position: absolute;
    left: 18px;
    top: 208px;
    margin: 0;
    font-family: "Frijole", cursive;
    font-size: 46px;
    color: var(--ink);
    -webkit-text-stroke: 1px var(--amber);
    transform: rotate(10deg);
    transform-origin: left top;
    letter-spacing: 1px;
  }
  .guitar-art {
    position: absolute;
    left: -20px;
    top: 470px;
    width: 940px;
    height: 210px;
    border-radius: 105px 40px 40px 105px;
    transform: rotate(-37deg);
    transform-origin: center;
    background: linear-gradient(90deg, rgba(59,53,18,0.95) 0%, rgba(59,53,18,0.85) 35%, rgba(59,53,18,0.45) 60%, rgba(59,53,18,0.7) 100%);
    filter: blur(2px);
  }
  .lineup {
    position: absolute;
    left: 0;
    top: 0;
    margin: 0;
    padding: 0;
    list-style: none;
  }
  .lineup li {
    position: absolute;
    white-space: nowrap;
    font-family: "Rye", serif;
    font-size: 48px;
    color: var(--band-fill);
    text-shadow: 0 0 4px var(--ink), 3px 3px 0 var(--ink), -2px -2px 0 var(--ink), 2px -2px 0 var(--ink), -2px 2px 0 var(--ink);
    transform: rotate(14deg);
    transform-origin: left top;
  }
  .lineup .act-1 { left: 293px; top: 362px; }
  .lineup .act-2 { left: 272px; top: 460px; }
  .lineup .act-3 { left: 252px; top: 556px; }
  .lineup .act-4 { left: 228px; top: 652px; }
  .tickets {
    position: absolute;
    right: 8px;
    top: 874px;
    margin: 0;
    text-align: right;
    font-family: "Russo One", sans-serif;
    font-size: 28px;
    color: var(--ink);
    font-style: italic;
    letter-spacing: 1px;
    line-height: 42px;
  }
  .tickets span {
    display: block;
    border-bottom: 1.5px solid var(--ink);
  }
  .tickets .bbq {
    border-bottom: none;
    color: var(--white);
    text-shadow: 2px 2px 0 var(--ink);
  }
  .details {
    position: absolute;
    left: 33px;
    top: 1014px;
    margin: 0;
    font-family: "Dosis", sans-serif;
    font-weight: 700;
    font-size: 27px;
    line-height: 41px;
    color: var(--white);
    text-transform: uppercase;
    text-shadow: 1px 1px 2px rgba(17,16,8,0.6);
  }
  .details span { display: block; }
</style>
</head>
<body>
<main class="poster">
  <div class="skyline-strip" role="img" aria-label="Row of small dark silhouette icons: city buildings, megaphone, stadium, stage, tower, trees"></div>

  <svg class="event-title" viewBox="0 0 848 70" aria-label="A Night Of Comets">
    <text x="8" y="50" textLength="834" lengthAdjust="spacingAndGlyphs">A NIGHT OF COMETS</text>
    <line x1="0" y1="62" x2="848" y2="62"/>
  </svg>

  <p class="tagline">LET US ROCK.....</p>

  <div class="guitar-art" role="img" aria-label="Large dark textured electric guitar silhouette lying diagonally across the poster"></div>

  <ul class="lineup">
    <li class="act-1">TURN THE DIAL</li>
    <li class="act-2">FROZEN FENWICK</li>
    <li class="act-3">WILMA'S LANTERN</li>
    <li class="act-4">LORALIE PETTIGREW</li>
  </ul>

  <p class="tickets">
    <span>TICKET PRICE: $10+BF ONLINE</span>
    <span>$15 AT THE DOOR</span>
    <span class="bbq">FREE BBQ!</span>
  </p>

  <p class="details">
    <span>Date: Saturday 10th November 2012</span>
    <span>Time: 5:15pm</span>
    <span>Venue: The Kiln, 47 Tamsin Street,</span>
    <span>West End, QLD 4101</span>
  </p>
</main>
</body>
</html>
```